Business Card Design

I am starting my therapy private practice. I will be an in home therapist, so I go into family's homes instead of using an office to do family/marriage therapy. Therefore, I do not have an office address. I am looking for something in the black, red, gray, and blue color scheme that appeals to both families, couples and teenagers.

Industry/Entity Type

Business

Contact Information for Business Card

Lena Brovick, MS, MFT Intern
Marriage and Family Therapy
In Home Therapist
508-241-6039
Lena@LenaBrovick.net

```html
<!DOCTYPE html>
<html lang="en">
<head>
<meta charset="utf-8">
<title>Lena Brovick — Business Card</title>
<link href="https://fonts.googleapis.com/css2?family=Tulpen+One&family=Montserrat:wght@300;400&display=swap" rel="stylesheet">
<style>
  :root {
    --page-bg: #b9bbbf;
    --card-black: #050505;
    --ink-white: #f4f4f4;
    --ink-gray: #c9c9c9;
    --red-bright: #e0201f;
    --red-mid: #a8171a;
    --red-dark: #2a0b08;
    --silver-light: #f2f2f2;
    --silver-mid: #9a9a9a;
    --silver-dark: #3a3a3a;
  }
  html, body {
    margin: 0;
    width: 1200px;
    height: 800px;
    overflow: hidden;
    background: var(--page-bg);
  }
  .business-card {
    position: absolute;
    left: 180px;
    top: 160px;
    width: 840px;
    height: 480px;
    background: var(--card-black);
    overflow: hidden;
    box-shadow: 0 10px 30px rgba(0,0,0,0.25);
  }
  .name {
    position: absolute;
    left: 0;
    right: 0;
    top: 60px;
    margin: 0;
    text-align: center;
    font-family: "Tulpen One", sans-serif;
    font-weight: 400;
    font-size: 128px;
    line-height: 1;
    letter-spacing: 14px;
    color: var(--ink-white);
    text-transform: uppercase;
  }
  .credentials {
    position: absolute;
    left: 430px;
    top: 188px;
    font-family: "Montserrat", sans-serif;
    font-weight: 400;
    font-size: 15px;
    letter-spacing: 2px;
    color: var(--ink-gray);
  }
  .specialty {
    position: absolute;
    left: 0;
    right: 0;
    top: 222px;
    margin: 0;
    text-align: center;
    font-family: "Tulpen One", sans-serif;
    font-size: 27px;
    letter-spacing: 3px;
    color: var(--ink-gray);
    text-transform: uppercase;
  }
  .silver-rule {
    position: absolute;
    left: 0;
    width: 100%;
    height: 7px;
    background: linear-gradient(90deg, var(--silver-dark) 0%, var(--silver-light) 35%, var(--silver-mid) 65%, var(--silver-dark) 100%);
  }
  .silver-rule.upper { top: 262px; }
  .silver-rule.middle { top: 392px; }
  .silver-rule.lower { top: 424px; }
  .contact-band {
    position: absolute;
    left: 0;
    top: 269px;
    width: 100%;
    height: 123px;
    background: radial-gradient(ellipse 70% 140% at 40% 50%, var(--red-bright) 0%, var(--red-mid) 45%, var(--red-dark) 100%);
  }
  .contact-line {
    position: absolute;
    left: 0;
    right: 0;
    margin: 0;
    text-align: center;
    font-family: "Montserrat", sans-serif;
    font-weight: 300;
    font-size: 25px;
    letter-spacing: 3px;
    color: var(--ink-white);
    text-transform: uppercase;
  }
  .contact-line.phone { top: 22px; }
  .contact-line.email { top: 70px; }
</style>
</head>
<body>
  <section class="business-card">
    <h1 class="name">Lena Brovick</h1>
    <span class="credentials">MS, MFT</span>
    <p class="specialty">Intern Marriage and Family Therapy In Home Therapist</p>
    <div class="silver-rule upper"></div>
    <div class="contact-band">
      <p class="contact-line phone">508-241-6039</p>
      <p class="contact-line email">Lena@LenaBrovick.net</p>
    </div>
    <div class="silver-rule middle"></div>
    <div class="silver-rule lower"></div>
  </section>
</body>
</html>
```